Business Card for Harborline Vessel

Hello, Will you do a business card design for Harborline Vessel? I attached a card from an old business of mine that I would like to copy.

The new info is:
Dennis Hollow
Owner
251-374-2908

Adress is:
41937 Pelican Ln, Orange Beach AL 36561

Email: dennis@harborlinevesselworks.example

Website is: www.harborlinevesselworks.example

Please use the new harborline vessel logo

Requirements
Must have
• QR Code for contact information

```html
<!DOCTYPE html>
<html lang="en">
<head>
<meta charset="utf-8">
<title>Harborline Vessel Works – Business Card</title>
<link href="https://fonts.googleapis.com/css2?family=Montserrat:wght@400;500;600;800&display=swap" rel="stylesheet">
<style>
  :root {
    --brand-red: #c92a26;
    --ink: #111111;
    --paper: #ffffff;
    --pattern-light: #f4f4f4;
    --pattern-mid: #e6e6e6;
    --code-fill: #d4d4d4;
    --backdrop: #d9d9d9;
  }
  * { box-sizing: border-box; margin: 0; padding: 0; }
  html, body {
    width: 1200px; height: 900px; overflow: hidden;
    background: var(--backdrop);
    font-family: "Montserrat", sans-serif;
  }
  .card {
    position: absolute; left: 320px;
    width: 560px; height: 320px;
    border-radius: 26px; overflow: hidden;
    box-shadow: 0 6px 18px rgba(0,0,0,0.18);
  }
  .card--front { top: 90px; background: var(--brand-red); }
  .card--back { top: 490px; background: var(--paper); }

  .front-wordmark {
    position: absolute; inset: 0;
    display: flex; flex-direction: column; align-items: center; justify-content: center;
    color: var(--paper); font-weight: 800; text-align: center;
    text-transform: uppercase; line-height: 1.05;
  }
  .front-wordmark__main { font-size: 62px; letter-spacing: 2px; }
  .front-wordmark__sub { font-size: 26px; letter-spacing: 4px; }

  .back-texture {
    position: absolute; inset: 0;
    background: linear-gradient(135deg, var(--pattern-light) 0%, var(--paper) 45%, var(--pattern-mid) 100%);
  }
  .back-wordmark {
    position: absolute; left: 60px; top: 36px;
    color: var(--ink); font-weight: 800; text-transform: uppercase;
    display: flex; align-items: center; gap: 10px;
  }
  .back-wordmark__dot { width: 16px; height: 16px; border-radius: 50%; background: var(--ink); }
  .back-wordmark__text { font-size: 24px; line-height: 1.05; letter-spacing: 1px; }
  .back-wordmark__text span { display: block; font-size: 11px; letter-spacing: 2px; }

  .contact-person {
    position: absolute; right: 44px; top: 112px; text-align: right;
  }
  .contact-person__name { color: var(--brand-red); font-size: 34px; font-weight: 600; line-height: 1.2; }
  .contact-person__role { color: var(--ink); font-size: 18px; font-weight: 600; margin-top: 2px; }
  .contact-person__phone {
    color: var(--brand-red); font-size: 24px; font-weight: 500; margin-top: 8px;
    display: flex; align-items: center; justify-content: flex-end; gap: 8px;
  }

  .contact-qr {
    position: absolute; right: 44px; bottom: 22px;
    width: 72px; height: 72px;
    background: var(--code-fill);
    border: 3px solid var(--ink);
    border-radius: 4px;
  }

  .contact-line {
    position: absolute; display: flex; align-items: flex-start; gap: 8px;
    color: var(--ink); font-size: 12.5px; font-weight: 500; line-height: 1.4;
  }
  .contact-line svg { flex: none; margin-top: 2px; }
  .contact-line--address { left: 40px; top: 128px; }
  .contact-line--email { left: 40px; top: 246px; font-size: 14px; }
  .contact-line--web { left: 40px; top: 272px; font-size: 12.5px; }
</style>
</head>
<body>
  <section class="card card--front" aria-label="Card front">
    <div class="front-wordmark">
      <div class="front-wordmark__main">Harborline</div>
      <div class="front-wordmark__sub">Vessel Works</div>
    </div>
  </section>

  <section class="card card--back" aria-label="Card back">
    <div class="back-texture" role="img" aria-label="Soft grey repeating hex-nut background pattern"></div>

    <div class="back-wordmark">
      <div class="back-wordmark__dot"></div>
      <div class="back-wordmark__text">Harborline<span>Vessel Works</span></div>
    </div>

    <div class="contact-line contact-line--address">
      <svg width="11" height="15" viewBox="0 0 12 16"><path d="M6 0C2.7 0 0 2.6 0 5.9 0 10.3 6 16 6 16s6-5.7 6-10.1C12 2.6 9.3 0 6 0zm0 8.2A2.3 2.3 0 1 1 6 3.6a2.3 2.3 0 0 1 0 4.6z" fill="#111"/></svg>
      <div>41937 Pelican Ln,<br>Orange Beach AL 36561</div>
    </div>

    <div class="contact-person">
      <div class="contact-person__name">Dennis Hollow</div>
      <div class="contact-person__role">Owner</div>
      <div class="contact-person__phone">
        <svg width="16" height="18" viewBox="0 0 16 18"><path d="M4 1l3 4-2 2c1 2.5 2.5 4.5 5 6l2-2 4 3-2 3C7 16 1 9 1 3z" fill="#c92a26"/></svg>
        251-374-2908
      </div>
    </div>

    <div class="contact-qr" role="img" aria-label="QR code with contact information"></div>

    <div class="contact-line contact-line--email">
      <svg width="16" height="12" viewBox="0 0 16 12"><rect width="16" height="12" rx="1" fill="#111"/><path d="M0 1l8 6 8-6" stroke="#fff" stroke-width="1.4" fill="none"/></svg>
      <div>dennis@harborlinevesselworks.example</div>
    </div>

    <div class="contact-line contact-line--web">
      <svg width="14" height="14" viewBox="0 0 14 14"><path d="M7 0l6 8H9v6H5V8H1z" fill="#111"/></svg>
      <div>www.harborlinevesselworks.example</div>
    </div>
  </section>
</body>
</html>
```